2 Sided Stunning and Attention Getting Brochure

Create an eye-catching, 2 sided brochure. The first side of the brochure includes the content provided in the attached word document. Make it a look incredibly professional, modern, and unique. The second side of the brochure are frequently asked questions. They includes the content of both PDFs on one page.

Target Market(s)

Birch Toolworks Store Owners. People who own Birch Toolworks stores.

Industry/Entity Type

Retail

Font styles to use
Serif

Colors
EB3D1F
EC4F4E
F09395
F8D3D4
FCEDEE

Requirements
Must have
• Birch Toolworks colors. Red, white, and black. Must be super creative, modernized, and different. Must catch my attention immediately and I must say "Now that's different looking!" Include Birch Toolworks logo and Qelmar Group logo. Google these.
Should not have
• Boring and dull. It has to be super creative and different.

```html
<!DOCTYPE html>
<html lang="en">
<head>
<meta charset="utf-8">
<title>Electronic Shelf Label FAQs — Birch Toolworks</title>
<link href="https://fonts.googleapis.com/css2?family=Raleway:wght@300;400;500;700;800&display=swap" rel="stylesheet">
<style>
  :root {
    --red: #e31b3a;
    --ink: #333333;
    --muted: #6a6a6a;
    --panel: #707070;
    --paper: #ffffff;
    --backdrop: #9a9a9a;
  }
  * { box-sizing: border-box; margin: 0; padding: 0; }
  html, body { width: 1199px; height: 1200px; overflow: hidden; }
  body {
    background: var(--backdrop);
    font-family: "Raleway", Arial, sans-serif;
    color: var(--ink);
    position: relative;
  }
  .sheet {
    position: absolute;
    top: 206px;
    width: 520px;
    height: 787px;
    background: var(--paper);
    overflow: hidden;
  }
  .sheet--front { left: 50px; }
  .sheet--back { left: 629px; }

  p, li { font-size: 7.6px; line-height: 1.34; color: var(--muted); }

  .faq-q {
    background: var(--red);
    color: #fff;
    font-weight: 800;
    font-size: 8px;
    line-height: 1.2;
    text-transform: uppercase;
    padding: 4px 10px 4px 28px;
    margin: 9px 0 4px;
  }
  .faq-a { padding: 0 10px 0 28px; }
  .faq-a p + p { margin-top: 6px; }
  .col-right .faq-q, .col-right .faq-a { padding-left: 8px; padding-right: 18px; }

  /* Brand name placeholder */
  .brand {
    position: absolute;
    display: flex;
    align-items: center;
    gap: 8px;
  }
  .brand__dot {
    width: 14px;
    height: 14px;
    border-radius: 50%;
    background: var(--red);
    flex: none;
  }
  .brand__name {
    font-weight: 800;
    color: var(--red);
    font-size: 19px;
    line-height: 1;
    white-space: nowrap;
  }

  /* Front */
  .title { position: absolute; left: 38px; top: 58px; }
  .title__kicker { font-size: 19px; font-weight: 400; color: #5d5d5d; }
  .title__main { font-size: 50px; font-weight: 800; color: var(--red); line-height: 1; margin-top: 4px; letter-spacing: 1px; }
  .sheet--front .brand { right: 26px; top: 82px; }
  .label-photo {
    position: absolute;
    left: 81px; top: 142px;
    width: 228px; height: 100px;
    background: linear-gradient(135deg, #d9d9d9 0%, #8c8c8c 45%, #c8b34a 70%, #e9e9e9 100%);
  }
  .col-left { position: absolute; left: 0; top: 310px; width: 278px; }
  .col-right { position: absolute; left: 284px; top: 222px; width: 236px; }

  /* Back */
  .sheet--back .brand { left: 46px; top: 118px; }
  .shelf-photo {
    position: absolute;
    left: 274px; top: 62px;
    width: 246px; height: 215px;
    background: linear-gradient(180deg, #e8e6e1 0%, #d4d2cc 55%, #bdbab3 100%);
  }
  .back-col { position: absolute; left: 0; top: 250px; width: 268px; }
  .back-col .faq-q { padding-left: 24px; }
  .back-col .faq-a { padding-left: 24px; padding-right: 10px; }
  .help-panel {
    position: absolute;
    left: 274px; top: 277px;
    width: 246px; height: 407px;
    background: var(--panel);
    padding: 104px 16px 0 16px;
  }
  .help-panel h3 { color: #fff; font-size: 7.8px; font-weight: 800; text-transform: uppercase; margin: 10px 0 4px; line-height: 1.2; }
  .help-panel p { color: #f1f1f1; }
  .help-panel p + p { margin-top: 6px; }
  .contact-band {
    position: absolute;
    left: 274px; top: 684px;
    width: 246px; height: 103px;
    background: var(--red);
    padding: 40px 16px 0;
  }
  .contact-band p { color: #fff; font-weight: 700; font-size: 7.6px; }
</style>
</head>
<body>

<section class="sheet sheet--front">
  <div class="title">
    <div class="title__kicker">Electronic Shelf Label</div>
    <div class="title__main">FAQs</div>
  </div>
  <div class="brand">
    <span class="brand__dot"></span>
    <span class="brand__name">Birch Toolworks</span>
  </div>
  <div class="label-photo" role="img" aria-label="Electronic shelf labels showing a sale price and a promotional yellow tag"></div>

  <div class="col-left">
    <h2 class="faq-q">Who is Birch Toolworks' preferred vendor for electronic shelf labels?</h2>
    <div class="faq-a"><p>QelmarGroup, a global leader in retail technology that specializes in cutting-edge in-store solutions for ESL automation and communication.</p></div>

    <h2 class="faq-q">At what stage is Birch at with the development of an ESL program?</h2>
    <div class="faq-a"><p>We are currently in the early stages of the program creation. Implementation and store procedure guides are being developed, and there are currently limited integration points with other Birch systems. As the program further matures, more functionality, tools, and resources are on the roadmap.</p></div>

    <h2 class="faq-q">Tell me about pricing. What tag sizes are offered and their corresponding pricing?</h2>
    <div class="faq-a"><p>Sizes and Prices are as follows:<br>·1.5" = $6.51 (smaller tag for tight spaces)/tag<br>·2.1" = $7.12 (most typically used)/tag<br>·4.2" = $15.62/tag<br>·7.4" = $35.24/tag</p></div>

    <h2 class="faq-q">In addition, a monthly SaaS fee (includes support, software, dashboards, etc.) applies:</h2>
    <div class="faq-a"><p>·Less than 10,000 tags = $100 a month<br>·Greater or equal to 10,000 tags = $200 a month<br>·Additional benefits available for retailers with 10 or more stores.</p></div>

    <h2 class="faq-q">Does Birch offer any financing plans for ESLs?</h2>
    <div class="faq-a"><p>Currently, a finance programs is not an option. As the program further develops, financial incentives will be re-assessed.</p></div>
  </div>

  <div class="col-right">
    <h2 class="faq-q">I heard the ESLs are considered 4-color Bluetooth technology. What does that even mean?</h2>
    <div class="faq-a"><p>Like the name states, there are four colors associated with tag displays (black, white, red, and yellow), which helps promo offerings, closeouts, etc. stand out amongst items. With its open protocol, Bluetooth technology allows for regular updates and continuous improvements. The 4-color Bluetooth electronic labels are the latest in digital price tag technology, enabling faster response times for ESL updates and ensuring improved performance and reliability. Bluetooth technology has an open protocol, meaning continuous advancements can be made to it.</p></div>

    <h2 class="faq-q">What does it mean that the ESL labels can "pick to light"</h2>
    <div class="faq-a"><p>Beyond price changes, ESLs have grown in capabilities to 'flash' to call further attention to product. This is helpful to find items quicker when assisting customers or for store associates to stock products. Birch feels there are several opportunities to create integration points with this feature and are targeting doing so in the future.</p></div>

    <h2 class="faq-q">Can I design different types of label depending on the item?</h2>
    <div class="faq-a"><p>Absolutely. Birch has set up recommended bin label "template designs" for each for the following types of tags:<br>• Standard, everyday items<br>• Items on promotion (specifically, items with a sales retail in Ledger MIP)<br>• Multiple Selling Unit (MSU) items, e.g. rope, wire, pipe<br>• Consumer Pricing Label</p></div>

    <h2 class="faq-q">Why is this beneficial?</h2>
    <div class="faq-a"><p>Based on the data from your system, the technology is smart enough to know which items are on (or coming off) an MIP promotion and automatically uses that bin label design at the shelf.</p></div>

    <h2 class="faq-q">How long does the battery of a shelf label last?</h2>
    <div class="faq-a"><p>Like with any battery, this varies from label to label based on the amount of use /number of updates to the tag. For illustrative purposes, if you average one price change per day, a battery can last up to eight years. Other factors driving battery life include the amount of tag pick-to-light 'flashing' performed.</p></div>
  </div>
</section>

<section class="sheet sheet--back">
  <div class="brand">
    <span class="brand__dot"></span>
    <span class="brand__name">Birch Toolworks</span>
  </div>
  <div class="shelf-photo" role="img" aria-label="Electronic shelf labels mounted on a store shelf edge showing oil filter pricing"></div>

  <div class="back-col">
    <h2 class="faq-q">Do the ESLs have any integration points with my POS?</h2>
    <div class="faq-a">
      <p>There are some degree of integration points between Orrin Ledger for Windows and ESLs. Via Beacon reporting, a process has been developed by which SKU files are sent throughout the day from Ledger to QelmarGroup (via store Access Points) recognizing changes to information appearing on the labels for updates. Tighter integration between ESLs and Orrin (including the Store Pocket App) are on the road-map for future pursuit.</p>
      <p>If you are on a different POS other than Orrin Ledger for Windows, integration is also possible, but you will need to collaborate with your POS provider on actions such as identifying the data feed for the ESL's, configuration setup, and the delivery mechanism to QelmarGroup.</p>
    </div>

    <h2 class="faq-q">Can I deploy labels for some of my store or is it all or nothing?</h2>
    <div class="faq-a"><p>The program is certainly flexible in terms of how much of your store you decide to pursue. You can start with an aisle or do the entire store. Bottomline - QelmarGroup can accommodate any size project.</p></div>

    <h2 class="faq-q">How do we associate ESLs with products in the store?</h2>
    <div class="faq-a"><p>"Linking" products to tags is most effectively executed via downloading QelmarGroup's app known as Q-link. This step-by-step process is covered in the ESL Implementation Guide.</p></div>

    <h2 class="faq-q">How do I determine my SKU count needs?</h2>
    <div class="faq-a"><p>There is item-level reporting available from Birch that can help you estimate your SKU count with filtering taking out potential "noise" data (i.e. HHC SKUS, non-priced items, service SKUs, etc.). These are estimated numbers, but should help to get you in the range of your overall needs.</p></div>

    <h2 class="faq-q">Can QelmarGroup do a lab setup?</h2>
    <div class="faq-a"><p>Of course, ESLs are an investment. As such, QelmarGroup is able to provide a lab set up in order to gain direct familiarity with the process. Just ask your QelmarGroup Sales Representative for details.</p></div>
  </div>

  <aside class="help-panel">
    <h3>What level of assistance will I receive with installation of tags?</h3>
    <p>There are two basic alternatives for installing ESLs:</p>
    <p>1. Standard do-it-yourself You will be trained on the process from QelmarGroup for you to self-deploy. Moreover, a step-by-step implementation guide and store procedures is in the process of being developed.</p>
    <p>2. White glove In this case, QelmarGroup and its partners install the fixtures, tags, and linking of labels to products for you. Request a quote from your Sales Representative for this service.</p>
    <h3>How do I get more information?</h3>
    <p>Conduct a discovery call with QelmarGroup. Visit the following webpage to get started:</p>
    <p>https://www.qelmar.example/birch-toolworks/</p>
    <p>You can also contact Marcus Hale, Business Development Manager at QelmarGroup, with any questions.</p>
  </aside>

  <div class="contact-band">
    <p>MARCUS.HALE@QELMAR.EXAMPLE<br>555.014.2290</p>
  </div>
</section>

</body>
</html>
```